HVRT LLP website - revamping our website after 23 years

Our website needs a complete overhaul. The purpose of this exercise is to provide us with your vision of what you think the website should look like. We don't need the website to be created or coded. Just need creative designs.

We have a four sites that we would like to base our website on;

We like the simplicity of Ravelstoke, the style of Pemberly Adair and Quillfeather.

http://www.pemberlyadair.example/en/toronto-ontario/
http://www.ravelstoke.example/
vintquillfeather.example
http://www.brindlemoor.example/our-professionals.html

We have a logo that we would like to use which will be attached below. We need to keep our website looking very professional as we have a large number of high net worth clients.
Updates

Hi, We've received some good website designs but they appear to be the same type of template websites we've received in the past - this is not what we're looking for. What we want is a unique website that is modelled on the following three company websites: http://www.ravelstoke.example/ www.vintquillfeather.example/ http://www.pemberlyadair.example/en/toronto-ontario/

Thank you everyone for your designs. I will be posting updates and my comments on the various designs in the next day - I want to thank you for the creative designs I see. I thought i would explain a bit about our firm and perhaps it can help when you design the theme of our website: - Our firm is like a family and our clients are truly like our friends. We have close knit relationships in and outside of the office with staff and clients. - We are an 'out of the box' type of firm. We operate differently than most firms and that's a differentiating factor in what makes us who we are - Our slogan is "Count on us" which is a testament to the way we run our practice - We would like an open, fresh, clean look to our website - we don't want the landing page to be overly long or complex because we have limited time to update the website and limited content That's it for the time being - when things come to mind I will post them here.

Can we try a design as follows: - make the website look very similar to www.ravelstoke.example - use the same background colour - Keep the same black top but insert our logo - incorporate some of the content from our current website www.hvrt-ca.example

I have been away dealing with a personal matter. I will look into these websites tomorrow afternoon and provide more feedback / info on the top designer. Thank you

Hi designers, I want to apologize for the delay. I plan on wrapping things up within the next few days. I will go through a few of the top designs and offer my comments. Thank you for your patience.

Target Market(s)

Mainly our current clients - We have a large number of high net worth individuals as clients.

Industry/Entity Type

Accounting

Number of Pages Required

1 page

Requirements
Must have
• Please model website on the websites indicated above.
• Our current website is www.hvrt-ca.example. It's dark, cluttered and not inviting. We want a fresh, clean website. Please incorporate the logo's attached below.

```html
<!DOCTYPE html>
<html lang="en">
<head>
<meta charset="utf-8">
<title>HVRT LLP — Services: Due Diligence</title>
<link href="https://fonts.googleapis.com/css2?family=Open+Sans:wght@400;600&display=swap" rel="stylesheet">
<style>
  :root{
    --header-bg:#3b3b3b;
    --footer-bg:#2f2f2f;
    --page-bg:#ffffff;
    --accent:#14c6f7;
    --accent-active:#27b3ee;
    --body-text:#8c8c8c;
    --title-text:#2b2b2b;
    --nav-text:#ffffff;
    --rule:#5e5e5e;
  }
  *{margin:0;padding:0;box-sizing:border-box}
  html,body{width:1200px;height:606px;overflow:hidden;background:var(--page-bg)}
  body{font-family:"Open Sans",Arial,sans-serif;position:relative}
  .site-header{position:absolute;left:0;top:0;width:1200px;height:83px;background:var(--header-bg)}
  .brand{position:absolute;left:234px;top:22px;display:flex;align-items:center;gap:8px}
  .brand-mark{width:22px;height:22px;background:var(--accent)}
  .brand-name{color:#fff;font-size:20px;font-weight:400;letter-spacing:.5px;line-height:1}
  .brand-tagline{position:absolute;left:234px;top:73px;font-size:5px;color:#ddd;letter-spacing:.3px}
  .main-nav{position:absolute;right:234px;top:22px;display:flex;gap:12px}
  .main-nav a{color:var(--nav-text);font-size:8.6px;font-weight:600;text-decoration:none;letter-spacing:-.1px}
  .main-nav a.is-current{color:var(--accent)}
  .main-nav a.links{position:relative;top:2px}
  .nav-rule{position:absolute;left:340px;top:59px;width:625px;height:1px;background:var(--rule)}
  .page-title{position:absolute;left:324px;top:95px;font-size:19px;font-weight:400;letter-spacing:1.2px;color:var(--title-text);white-space:nowrap}
  .page-title span{color:var(--accent)}
  .copy{position:absolute;font-size:8.7px;line-height:15px;color:var(--body-text);letter-spacing:-.1px}
  .copy p{margin-bottom:15px}
  .copy-left{left:274px;top:135px;width:310px}
  .copy-right{left:620px;top:366px;width:345px}
  .copy-right p{margin:0}
  .feature-image{position:absolute;left:619px;top:134px;width:344px;height:164px;
    background:linear-gradient(120deg,#f3f6fa 0%,#c9d6e6 45%,#6f8bb0 75%,#2b4a78 100%)}
  .submenu{position:absolute;left:751px;top:67px;width:212px;height:240px;background:var(--accent);list-style:none;padding-top:9px}
  .submenu li{height:19.6px;line-height:19.6px;padding-left:14px;font-size:8.4px;font-weight:600;color:#fff;text-transform:uppercase;white-space:nowrap;letter-spacing:-.1px}
  .submenu li.is-active{background:var(--accent-active);width:232px;padding-left:58px}
  .site-footer{position:absolute;left:0;top:549px;width:1200px;height:57px;background:var(--footer-bg)}
  .footer-links,.copyright{position:absolute;right:237px;font-size:8.7px;color:var(--accent);white-space:nowrap}
  .footer-links{top:15px}
  .copyright{top:30px}
  .footer-links a{color:var(--accent);text-decoration:none}
</style>
</head>
<body>
  <header class="site-header">
    <div class="brand"><span class="brand-mark"></span><span class="brand-name">HVRT LLP</span></div>
    <div class="brand-tagline">CHARTERED PROFESSIONAL ACCOUNTANTS</div>
    <nav class="main-nav">
      <a href="#">HOME</a>
      <a href="#">ABOUT HVRT</a>
      <a href="#" class="is-current">CERVICES</a>
      <a href="#">LIBRARY</a>
      <a href="#" class="links">LINKS</a>
      <a href="#">CAREERS</a>
      <a href="#">CONTACTS</a>
    </nav>
    <div class="nav-rule"></div>
  </header>

  <h1 class="page-title"><span>CERVICES</span> : DUE DILIGENCE</h1>

  <div class="copy copy-left">
    <p>Due Diligence. What is it?</p>
    <p>In a commercial context, it is the process of determining that information and representations are accurate, or at least reasonable in the circumstances. This process is generally conducted by an independent third party.</p>
    <p>This financial due diligence may be required by a purchaser or minority inves-tor in the course of a purchase/sale of a business or some form of business combination. It may also be required by investors and lenders in a (re)financing arrangement.</p>
    <p>At HVRT we have developed the "art" of due diligence to a new level. Our approach is not simply to check for numbers and documents. We strive to find out what makes a business tick. What makes it successful? What are the critical areas that could adversely effect a business? This approach is vital, especially when preparing or reviewing management prepared business forecasts.</p>
    <p style="margin-top:30px">Whether working with a financial institution, lawyer or principal investor/purchaser, we believe that we are especially suited to provide this service to the small and mid market business sector, whether for the private owner managed business or for a public company.</p>
    <p>A brief sampling of some of the transactions in which we have played a key role include:</p>
  </div>

  <div class="feature-image" role="img" aria-label="Photograph of a financial spreadsheet with a pair of reading glasses resting on it"></div>

  <ul class="submenu">
    <li>&nbsp;Accounting and Auditing</li>
    <li>Business Advisory</li>
    <li class="is-active">Due Diligence</li>
    <li>High-Tech Industry</li>
    <li>Investors and Wealth&nbsp; Management</li>
    <li>Medical Professionals</li>
    <li>Not for Profit and&nbsp; Charitable Sector</li>
    <li>Personal Tax Services</li>
    <li>The Legal Profession</li>
    <li>The Real Estate Industry</li>
    <li>Tax Planning and&nbsp; Compliance</li>
  </ul>

  <div class="copy copy-right">
    <p>two separate private placements in publicly traded food processing and distribution companies, outright purchase of major machine shop and fabrication division of a large multinational corporation, equity and subordinated debt investment in beverage opera-tion, followed-up with subsequent merger with a second beverage processor, and equity and subordinated debt investment in companies in the following industries: foundry operations,</p>
    <p>manufacturer and distributor of packaging and storage products,</p>
    <p>photo-finishing lab, and glass and plastic recycling.</p>
    <p>We believe that our experience and our commitment to getting it right, along with our approach to each and every assignment makes us a well suited alternative to the national accounting firms, in the due diligence arena.</p>
  </div>

  <footer class="site-footer">
    <div class="footer-links"><a href="#">Site Map</a> | <a href="#">AODA</a> &nbsp;|&nbsp; <a href="#">Privacy Policy</a></div>
    <div class="copyright">© 2006 HVRT Chartered Accountants. All rights reserved.</div>
  </footer>
</body>
</html>
```